Help a start up law firm make an impression! - Website

We are a property development and conveyancing law firm looking for some to design our website. The initial brief is for 6 pages with scope for on-going work.

Law firms are traditionally quite conservative and we want to break the mold. We want to come across as fun and modern, while still being professional.

A good example is https://quorrantlaw.com.au/. It's professional yet modern.
Updates

Another good site I like in the same industry: https://www.tindalemarshconveyancing.com.au/

Target Market(s)

Tech savy home buyers and sellers - generally 30 to 50 years old

Industry/Entity Type

Law Firm

Coding

Coded - Design and coding required

Number of Pages Required

5+ page

Font styles to use
Other font styles liked:
• No idea

Colors
f04a50

Requirements
Must have
• The elements set out in the design brief document

```html
<!DOCTYPE html>
<html lang="en">
<head>
<meta charset="utf-8">
<title>Harwell Law – The Property Law Experts</title>
<link href="https://fonts.googleapis.com/css2?family=Lato:wght@400;700;900&display=swap" rel="stylesheet">
<style>
:root{
  --brand:#c4465a;
  --brand-dark:#a93a4c;
  --ink:#1d1d1f;
  --body:#555;
  --white:#fff;
  --line:#e3a9b2;
  --footer-line:#e6e6e6;
}
*{box-sizing:border-box;margin:0;padding:0}
html,body{width:1200px;height:3502px;overflow:hidden}
body{position:relative;background:var(--white);font-family:'Lato',sans-serif;color:var(--ink)}
.abs{position:absolute}

/* hero */
.hero{left:0;top:0;width:1200px;height:572px;background:linear-gradient(180deg,#3d6f95 0%,#2b4a6e 40%,#1b2240 70%,#3a2a3a 100%)}
.brand-name{font-weight:900;color:var(--white);font-size:34px;letter-spacing:.5px}
.hero .brand-name{left:98px;top:50px}
.call{left:780px;top:40px;display:flex;align-items:center;gap:16px;color:var(--white)}
.call-icon{width:46px;height:46px;border-radius:50%;background:var(--brand);display:flex;align-items:center;justify-content:center}
.call small{display:block;font-size:13px;font-weight:700;letter-spacing:.3px}
.call strong{display:block;font-size:21px;font-weight:900}
.menu{left:1068px;top:52px;width:30px}
.menu span{display:block;height:4px;background:var(--white);margin-bottom:6px;border-radius:2px}
.hero-title{left:0;top:198px;width:1200px;text-align:center;color:var(--white);font-weight:900;font-size:66px;letter-spacing:-.5px}
.hero-sub{left:0;top:280px;width:1200px;text-align:center;color:var(--white);font-size:22px;font-weight:700}
.btn{display:inline-block;border-radius:30px;font-weight:900;text-transform:uppercase;text-align:center}
.hero-btn{left:500px;top:332px;width:200px;height:50px;line-height:48px;background:var(--brand);color:var(--white);font-size:16px;border:2px solid #e88896}
.dots{left:568px;top:504px;display:flex;gap:6px}
.dots span{width:13px;height:13px;border-radius:50%;border:2px solid var(--white)}
.dots span:first-child{background:var(--white)}

/* features */
.feature{top:700px;width:233px;height:281px;border:2px solid var(--line);text-align:center;padding:90px 22px 0}
.feature-icon{position:absolute;top:-44px;left:72px;width:88px;height:88px;border-radius:50%;background:var(--brand);display:flex;align-items:center;justify-content:center}
.feature h3{font-size:16px;font-weight:900;margin-bottom:14px}
.feature p{font-size:12px;line-height:1.75;color:var(--body)}

/* services */
.photo{display:block}
.service-title{color:var(--white);font-weight:900;font-size:31px;letter-spacing:.3px}
.service-text{color:var(--white);font-size:13px;line-height:1.9;width:470px}
.service-btn{background:var(--white);color:var(--ink);font-size:12px;width:120px;height:36px;line-height:36px}

/* blog */
.section-title{left:0;width:1200px;text-align:center;font-weight:900;font-size:30px}
.post{top:2099px;width:323px}
.post-photo{height:185px}
.post h4{margin-top:44px;font-size:17px;font-weight:700}
.post p{margin-top:14px;font-size:12px;line-height:2.1;color:var(--body)}
.post a{display:block;margin-top:10px;font-size:12px;font-weight:900;color:var(--brand);text-decoration:none}

/* contact */
.contact{left:0;top:2529px;width:1200px;height:595px;background:linear-gradient(160deg,#1c2a44 0%,#3a4d6b 45%,#1a2438 100%)}
.contact-title{top:2596px;color:var(--white)}
.contact-sub{left:0;top:2646px;width:1200px;text-align:center;color:var(--white);font-size:15px;font-weight:700}
.field{background:var(--white);font-size:13px;color:#666;padding:12px 14px}
.contact-btn{left:521px;top:3000px;width:160px;height:50px;line-height:50px;background:var(--brand);color:var(--white);font-size:16px}

/* footer */
.footer .brand-name{color:var(--ink);left:98px;top:3266px;font-size:34px}
.footer h5{font-size:16px;font-weight:700;margin-bottom:18px}
.footer ul{list-style:none;font-size:12px;line-height:2.1;color:var(--body)}
.footer p{font-size:12px;line-height:1.9;color:var(--body)}
.news-input{margin-top:16px;border-bottom:1px solid #ccc;padding:6px 12px;font-size:11px;color:#aaa;width:248px}
.subscribe{margin-top:16px;border:2px solid var(--brand);color:var(--brand);font-size:11px;width:98px;height:30px;line-height:26px}
.contact-row{display:flex;align-items:flex-start;gap:18px;font-size:12px;line-height:1.7;color:var(--body);margin-bottom:18px}
.footer-rule{left:98px;top:3423px;width:1004px;height:1px;background:var(--footer-line)}
.copyright{left:98px;top:3452px;font-size:12px;color:var(--body)}
.social{left:975px;top:3445px;display:flex;gap:10px}
.social span{width:28px;height:28px;border-radius:50%;border:1.5px solid var(--brand)}
</style>
</head>
<body>

<!-- HERO -->
<section class="abs hero" role="img" aria-label="Night city skyline with a lit bridge reflected on the river"></section>
<div class="abs brand-name">Harwell Law</div>
<div class="abs call">
  <span class="call-icon"><svg width="22" height="22" viewBox="0 0 24 24"><path fill="#fff" d="M6.6 10.8a15 15 0 0 0 6.6 6.6l2.2-2.2c.3-.3.7-.4 1-.2 1.1.4 2.3.6 3.6.6.6 0 1 .4 1 1V20c0 .6-.4 1-1 1A17 17 0 0 1 3 4c0-.6.4-1 1-1h3.5c.6 0 1 .4 1 1 0 1.3.2 2.5.6 3.6.1.3 0 .7-.2 1z"/></svg></span>
  <span><small>CALL OUR EXPERTS TODAY</small><strong>1.800.555.0142</strong></span>
</div>
<div class="abs menu"><span></span><span></span><span></span></div>
<h1 class="abs hero-title">THE PROPERTY LAW EXPERTS</h1>
<p class="abs hero-sub">Unrivaled response times, fixed fee options and experienced property lawyers</p>
<a class="abs btn hero-btn">GET MORE INFO</a>
<div class="abs dots"><span></span><span></span><span></span><span></span></div>

<!-- FEATURES -->
<div class="abs feature" style="left:98px">
  <div class="feature-icon"><svg width="40" height="30" viewBox="0 0 40 30"><rect x="2" y="4" width="36" height="22" rx="2" fill="none" stroke="#fff" stroke-width="3"/><circle cx="20" cy="15" r="6" fill="#fff"/></svg></div>
  <h3>COST CERTAINTY</h3>
  <p>Flexible fee arrangements with no surprises. We offer fixed fee, pay on completion and monthly retainer options to suit your needs.</p>
</div>
<div class="abs feature" style="left:354px">
  <div class="feature-icon"><svg width="42" height="34" viewBox="0 0 42 34"><circle cx="21" cy="9" r="6" fill="#fff"/><circle cx="9" cy="12" r="4.5" fill="#fff"/><circle cx="33" cy="12" r="4.5" fill="#fff"/><path d="M11 32c0-8 4-14 10-14s10 6 10 14z" fill="#fff"/><path d="M1 30c0-6 3-11 8-11 2 0 3 .5 4 1.5-2 3-3 6-3 9.5z M41 30c0-6-3-11-8-11-2 0-3 .5-4 1.5 2 3 3 6 3 9.5z" fill="#fff"/></svg></div>
  <h3>EXPERT LAWYERS</h3>
  <p>Our experienced team has managed over 2,000 conveyances and worked on some of the most iconic developments in Queensland. All we do is property law, all day everyday.</p>
</div>
<div class="abs feature" style="left:609px">
  <div class="feature-icon"><svg width="40" height="36" viewBox="0 0 40 36"><circle cx="14" cy="20" r="9" fill="none" stroke="#fff" stroke-width="5" stroke-dasharray="4 3"/><circle cx="30" cy="9" r="6" fill="none" stroke="#fff" stroke-width="4" stroke-dasharray="3 2.5"/></svg></div>
  <h3>RESPONSIVE SERVICE</h3>
  <p>The most responsive service, guaranteed. No more waiting days for a lawyer to respond to your email, return your call or prepare your contract.</p>
</div>
<div class="abs feature" style="left:866px">
  <div class="feature-icon"><svg width="40" height="34" viewBox="0 0 40 34"><ellipse cx="16" cy="13" rx="14" ry="10" fill="none" stroke="#fff" stroke-width="3"/><path d="M8 21l-3 8 9-5" fill="#fff"/><path d="M30 12c5 1 8 5 8 9 0 3-2 5-4 7l2 5-7-3c-5 1-10-1-12-4" fill="none" stroke="#fff" stroke-width="3"/></svg></div>
  <h3>COMMERCIAL ADVICE</h3>
  <p>We work with you to get the deal done without legal jargon getting in the way. We understand timing is crucial and we focus on the legal issues that are important to you.</p>
</div>

<!-- SERVICES -->
<div class="abs photo" style="left:0;top:1081px;width:605px;height:425px;background:linear-gradient(160deg,#cfd9e4 0%,#a9a28a 45%,#6f8a3d 80%,#8a2b2b 100%)" role="img" aria-label="Suburban house with a sold for-sale sign on the front lawn"></div>
<div class="abs" style="left:605px;top:1081px;width:595px;height:425px;background:var(--brand)"></div>
<svg class="abs" style="left:980px;top:1081px" width="220" height="110" viewBox="0 0 220 110"><polygon points="0,0 220,0 220,110" fill="#fff"/></svg>
<h2 class="abs service-title" style="left:697px;top:1158px">CONVEYANCING SERVICES</h2>
<p class="abs service-text" style="left:697px;top:1216px">Looking for off the plan contracts, joint venture agreements, management rights sale agreements, caretaking agreements, letting agreements and more? If it's related to property development, Harwell Law can help.<br><br>We offer a comprehensive service from site acquisition through to conveyancing of finished stock.</p>
<a class="abs btn service-btn" style="left:697px;top:1396px">READ MORE</a>

<div class="abs" style="left:0;top:1506px;width:605px;height:420px;background:var(--brand)"></div>
<svg class="abs" style="left:0;top:1366px" width="605" height="141" viewBox="0 0 605 141"><polygon points="0,0 605,141 0,141" fill="var(--brand)"/></svg>
<div class="abs photo" style="left:605px;top:1506px;width:595px;height:420px;background:linear-gradient(180deg,#c9a9c8 0%,#e9b79a 45%,#4b5d78 75%,#2f3f52 100%)" role="img" aria-label="Construction cranes over a high-rise building site at dusk"></div>
<svg class="abs" style="left:1100px;top:1506px" width="100" height="40" viewBox="0 0 100 40"><polygon points="0,0 100,0 100,40" fill="var(--brand)"/></svg>
<svg class="abs" style="left:0;top:1925px" width="240" height="106" viewBox="0 0 240 106"><polygon points="0,0 240,0 0,106" fill="var(--brand)"/></svg>
<h2 class="abs service-title" style="left:98px;top:1597px">DEVELOPMENT LAW SERVICES</h2>
<p class="abs service-text" style="left:98px;top:1655px">Looking for off the plan contracts, joint venture agreements, management rights sale agreements, caretaking agreements, letting agreements and more? If it's related to property development, Harwell Law can help.<br><br>We offer a comprehensive service from site acquisition through to conveyancing of finished stock.</p>
<a class="abs btn service-btn" style="left:98px;top:1834px">READ MORE</a>

<!-- BLOG -->
<h2 class="abs section-title" style="top:2024px">RECENT BLOG POSTS</h2>
<article class="abs post" style="left:98px">
  <div class="post-photo" style="background:linear-gradient(135deg,#8ab8e0,#2e5e90)" role="img" aria-label="Business silhouettes by an office window"></div>
  <h4>Real estate laws on the move</h4>
  <p>Neque porro quisquam est, qui dolorem ipsum quia dolor sit amet, consectetur, adipisci.</p>
  <a>READ MORE</a>
</article>
<article class="abs post" style="left:439px">
  <div class="post-photo" style="background:linear-gradient(135deg,#dce6ef,#7c8fa3)" role="img" aria-label="Businessmen talking in a bright office"></div>
  <h4>Private equity firm takes control</h4>
  <p>Neque porro quisquam est, qui dolorem ipsum quia dolor sit amet, consectetur, adipisci.</p>
  <a>READ MORE</a>
</article>
<article class="abs post" style="left:777px">
  <div class="post-photo" style="background:linear-gradient(135deg,#eef0f2,#9aa3ad)" role="img" aria-label="Colleagues working on laptops at a meeting table"></div>
  <h4>Technology changing laws</h4>
  <p>Neque porro quisquam est, qui dolorem ipsum quia dolor sit amet, consectetur, adipisci.</p>
  <a>READ MORE</a>
</article>

<!-- CONTACT -->
<section class="abs contact" role="img" aria-label="Looking up at office towers against the sky"></section>
<h2 class="abs section-title contact-title">GET IN TOUCH</h2>
<p class="abs contact-sub">Fill out the form below to get in touch. A Harwell Law team member will be in touch shortly!</p>
<div class="abs field" style="left:257px;top:2709px;width:338px;height:42px">First Name*</div>
<div class="abs field" style="left:607px;top:2709px;width:334px;height:42px">Last Name*</div>
<div class="abs field" style="left:257px;top:2765px;width:338px;height:42px">Email Address*</div>
<div class="abs field" style="left:607px;top:2765px;width:334px;height:42px">Phone Number</div>
<div class="abs field" style="left:257px;top:2818px;width:684px;height:164px">Message</div>
<a class="abs btn contact-btn">GET IN TOUCH</a>

<!-- FOOTER -->
<footer class="footer">
  <div class="abs brand-name">Harwell Law</div>
  <div class="abs" style="left:418px;top:3198px">
    <h5>Quick Links</h5>
    <ul><li>Home</li><li>Conveyancing</li><li>Property Development</li><li>News &amp; Knowledge</li><li>About us</li><li>Contact us</li></ul>
  </div>
  <div class="abs" style="left:586px;top:3198px;width:260px">
    <h5>Newsletter Subscription</h5>
    <p>Register your Email Address to get information about us</p>
    <div class="news-input">Email Address</div>
    <div class="btn subscribe">SUBSCRIBE</div>
  </div>
  <div class="abs" style="left:873px;top:3198px;width:240px">
    <h5>Contact Us</h5>
    <div class="contact-row"><svg width="12" height="16" viewBox="0 0 12 16"><path d="M6 0a6 6 0 0 1 6 6c0 4-6 10-6 10S0 10 0 6a6 6 0 0 1 6-6z" fill="var(--brand)"/><circle cx="6" cy="6" r="2.2" fill="#fff"/></svg><span>4820 Harbour Lane Brisbane,<br>QLD 4000</span></div>
    <div class="contact-row"><svg width="14" height="14" viewBox="0 0 24 24"><path fill="var(--brand)" d="M6.6 10.8a15 15 0 0 0 6.6 6.6l2.2-2.2c.3-.3.7-.4 1-.2 1.1.4 2.3.6 3.6.6.6 0 1 .4 1 1V20c0 .6-.4 1-1 1A17 17 0 0 1 3 4c0-.6.4-1 1-1h3.5c.6 0 1 .4 1 1 0 1.3.2 2.5.6 3.6.1.3 0 .7-.2 1z"/></svg><span>1.800.555.0142</span></div>
    <div class="contact-row"><svg width="14" height="12" viewBox="0 0 14 12"><rect width="14" height="12" rx="1" fill="var(--brand)"/><path d="M1 2l6 4.5L13 2" fill="none" stroke="#fff" stroke-width="1.3"/></svg><span>hello@harwelllaw.com</span></div>
  </div>
  <div class="abs footer-rule"></div>
  <p class="abs copyright">Copyrights © 2017, Harwell Law. All rights reserved.</p>
  <div class="abs social"><span></span><span></span><span></span><span></span></div>
</footer>

</body>
</html>
```